Divorce Lawyer Creative Business Card Design Project

Need a fresh look for our business cards that incorporates our current logo. We have three attorneys and six staff. Some will also use a Q/R Code (which is personal to the staff member) and that should be incorporated into the design so that we have a "with Q/R Code option" and a "without Q/R Code option"
While our business is serious and we want to be professional, we also welcome a bit of creativity and "fun." See http://quillmarten.example/creative-business-card-for-a-divorce-lawyer/ for a unique divorce lawyer business card. It is cool but the card itself is boring...
We add new people, change titles, some of our staff get married (and divorced) and have name changes and we need the ability to use a design template that you provide to make these changes ourselves. We usually print our cards at Orno Press.
I have uploaded a file that contains a sample of our current front and back of the business card as well as a sample Q/R Contact code to be included on a card. Obviously, we like the design that we have which should give you a feel for us but we are ready for a fresh look.
If you can't provide a design that we can manipulate, we will need .eps, .pdf, and .jpg files for three attorneys and six staff.
Updates
- Layout for this card is really nice: http://blog.inkholt.example/wp-content/uploads/2013/03/tovra-business-card.jpg
- This is creative: http://pinboardly.example/pin/502817364920175438/ but I don't really like it.
- Plastic is kind of cool: http://pinboardly.example/pin/502817364920331642/
- DISLIKE: http://brandvaultly.example/sites/default/files/styles/media/public/images/Lawyerbusinesscard.jpg?itok=ZmRtWx-k
- This is really cool but I fear the printing costs would be too high: http://pinboardly.example/pin/61520487390254718/
- I am not opposed to different but similar designs: See http://www.folionest.example/gallery/ZEP-Business-Cards/8260534
Industry/Entity Type
Lawyer
Requirements
Must have
- Our Logo
Person's Full Name
Title
Phone #
Fax #
Email
Web Address

```html
<!DOCTYPE html>
<html lang="en">
<head>
<meta charset="utf-8">
<title>Birch Law – Business Card</title>
<link rel="stylesheet" href="https://fonts.googleapis.com/css2?family=Roboto:wght@300;400&display=swap">
<style>
  :root {
    --backdrop: #a7a8ab;
    --card: #e6e7e8;
    --ink: #4a4a4c;
    --ink-strong: #2e2e30;
    --heart: #ec1c24;
    --navy: #27386b;
    --cut: #111111;
  }
  * { box-sizing: border-box; margin: 0; padding: 0; }
  html, body {
    width: 1200px; height: 900px; overflow: hidden;
    background: var(--backdrop);
    font-family: "Roboto", Arial, sans-serif;
    font-weight: 300;
    color: var(--ink);
  }
  .stage { position: relative; width: 1200px; height: 900px; }

  .card-clip { position: absolute; overflow: hidden; background: var(--card); height: 307px; }
  .card-face { position: absolute; top: 0; width: 526px; height: 307px; }

  .whole-card { left: 56px; top: 233px; width: 526px; }
  .whole-card .card-face { left: 0; }

  .tear-strip { left: 613px; top: 347px; width: 79px; }
  .tear-strip .card-face { left: 0; }
  .tear-main { left: 704px; top: 347px; width: 447px; }
  .tear-main .card-face { left: -79px; }

  .heart { position: absolute; left: 16px; top: 119px; width: 125px; height: 105px; }
  .heart path { fill: var(--heart); }

  .cut-line {
    position: absolute; left: 78px; top: 0; height: 307px;
    border-left: 2px dashed var(--cut);
  }
  .tear-strip .cut-line, .tear-main .cut-line { display: none; }

  .brand {
    position: absolute; left: 398px; top: 30px; width: 100px;
    display: flex; align-items: center; gap: 6px;
    color: var(--navy); font-weight: 400; font-size: 17px; letter-spacing: 0.5px;
  }
  .brand-square { width: 12px; height: 12px; background: var(--navy); flex: none; }

  .contact { position: absolute; left: 168px; top: 122px; }
  .contact-name { font-size: 21px; color: var(--ink-strong); line-height: 1.1; }
  .contact-title { font-size: 15px; margin-top: 4px; }
  .contact-block { font-size: 15px; line-height: 19px; }
  .address { margin-top: 14px; }
  .po-box { margin-top: 10px; }
  .reach { margin-top: 11px; }
</style>
</head>
<body>
<main class="stage">

  <section class="card-clip whole-card" aria-label="Business card, uncut">
    <div class="card-face">
      <svg class="heart" viewBox="0 0 100 84" aria-hidden="true"><path d="M50 84 L8 44 C-6 30 2 4 26 2 C38 1 46 8 50 16 C54 8 62 1 74 2 C98 4 106 30 92 44 Z"/></svg>
      <div class="cut-line"></div>
      <div class="brand"><span class="brand-square"></span><span>Birch Law</span></div>
      <div class="contact">
        <p class="contact-name">Daniel Avery Holt</p>
        <p class="contact-title">Managing Attorney</p>
        <p class="contact-block address">Counsel Court-Suite G, 218 Linden Street<br>Harborton, NC 28455</p>
        <p class="contact-block po-box">P.O. Box 412, Harborton, NC 28456</p>
        <p class="contact-block reach">Phone: (555) 014-2287, Fax: (555) 014-6390<br>dholt@birchfamilylaw.example</p>
      </div>
    </div>
  </section>

  <section class="card-clip tear-strip" aria-hidden="true">
    <div class="card-face">
      <svg class="heart" viewBox="0 0 100 84"><path d="M50 84 L8 44 C-6 30 2 4 26 2 C38 1 46 8 50 16 C54 8 62 1 74 2 C98 4 106 30 92 44 Z"/></svg>
    </div>
  </section>

  <section class="card-clip tear-main" aria-label="Business card, torn along the heart">
    <div class="card-face">
      <svg class="heart" viewBox="0 0 100 84" aria-hidden="true"><path d="M50 84 L8 44 C-6 30 2 4 26 2 C38 1 46 8 50 16 C54 8 62 1 74 2 C98 4 106 30 92 44 Z"/></svg>
      <div class="brand"><span class="brand-square"></span><span>Birch Law</span></div>
      <div class="contact">
        <p class="contact-name">Daniel Avery Holt</p>
        <p class="contact-title">Managing Attorney</p>
        <p class="contact-block address">Counsel Court-Suite G, 218 Linden Street<br>Harborton, NC 28455</p>
        <p class="contact-block po-box">P.O. Box 412, Harborton, NC 28456</p>
        <p class="contact-block reach">Phone: (555) 014-2287, Fax: (555) 014-6390<br>dholt@birchfamilylaw.example</p>
      </div>
    </div>
  </section>

</main>
</body>
</html>
```